Events floral designer business needs a logo design

I need a logo design for my floral design business called tender thorns.
i am inspired by nature and the simplicity of its beauty, whilst upcycling and recycling materials to reduce waste and impact on our environment.
I would like the design to be printed on recycled brown cardboard so i would like a simple but striking design of a bold black ivy vine or gnarly magnolia or tree branch with lower case old school type writer font.

Target Market(s)

Anyone requiring floral additions for their event

Industry/Entity Type

Business

Contact Information for Business Card

mara hollis
floral designer/creator
0418657203
mara@tenderthorns.com
tenderthorns.com

Font styles to use
Other font styles liked:
• lower case type writer

Colors
000000

Requirements
Must have
• simplicity but boldness
• Black typewriter font and bold picture with my details
Nice to have
• as above
Should not have
• colour

```html
<!DOCTYPE html>
<html lang="en">
<head>
<meta charset="utf-8">
<title>Tender Thorns – Business Card</title>
<link rel="stylesheet" href="https://fonts.googleapis.com/css2?family=Special+Elite&family=Open+Sans:wght@400;500&display=swap">
<style>
  :root {
    --backdrop: #5e5e5e;
    --card-light: #f2f2f2;
    --card-dark: #2a2a2a;
    --ink: #1a1a1a;
    --ink-soft: #222222;
    --dark-mark: #333333;
    --light-type: #e8e8e8;
  }
  html, body {
    margin: 0;
    padding: 0;
    width: 1200px;
    height: 900px;
    overflow: hidden;
    background: var(--backdrop);
  }
  .stage {
    position: relative;
    width: 1200px;
    height: 900px;
  }
  .card {
    position: absolute;
    top: 170px;
    width: 347px;
    height: 561px;
    overflow: hidden;
  }
  .card--front {
    left: 259px;
    background: var(--card-light);
    color: var(--ink);
  }
  .card--back {
    left: 631px;
    background: var(--card-dark);
  }
  .brand-mark {
    position: absolute;
    left: 131px;
    top: 98px;
    width: 86px;
    height: 86px;
    border-radius: 50%;
    background: var(--ink);
  }
  .brand-name {
    position: absolute;
    left: 0;
    width: 100%;
    text-align: center;
    font-family: "Special Elite", "Courier New", monospace;
    letter-spacing: 1px;
    white-space: nowrap;
    margin: 0;
    font-weight: 400;
  }
  .card--front .brand-name {
    top: 206px;
    font-size: 32px;
    color: var(--ink);
  }
  .card--back .brand-name {
    top: 467px;
    font-size: 38px;
    color: var(--light-type);
  }
  .back-mark {
    position: absolute;
    left: 16px;
    top: 110px;
    width: 300px;
    height: 300px;
    border-radius: 50%;
    background: var(--dark-mark);
  }
  .person {
    position: absolute;
    left: 0;
    top: 358px;
    width: 100%;
    text-align: center;
    font-family: "Open Sans", Arial, sans-serif;
  }
  .person__name {
    margin: 0;
    font-size: 20px;
    font-weight: 500;
    letter-spacing: 0.5px;
    line-height: 28px;
    color: var(--ink-soft);
  }
  .person__role {
    margin: 0;
    font-size: 15px;
    line-height: 20px;
    color: var(--ink-soft);
  }
  .contact {
    position: absolute;
    left: 0;
    top: 442px;
    width: 100%;
    text-align: center;
    font-family: "Open Sans", Arial, sans-serif;
    font-size: 15px;
    line-height: 20.5px;
    color: var(--ink-soft);
  }
  .contact__icons {
    display: flex;
    justify-content: center;
    gap: 5px;
    height: 12px;
    margin-bottom: 5px;
  }
  .contact__icons svg {
    width: 11px;
    height: 11px;
    fill: var(--ink-soft);
  }
  .contact__line {
    margin: 0;
  }
</style>
</head>
<body>
<main class="stage">
  <section class="card card--front" aria-label="Business card front">
    <div class="brand-mark" aria-hidden="true"></div>
    <h1 class="brand-name">TENDER THORNS</h1>
    <div class="person">
      <p class="person__name">MARA HOLLIS</p>
      <p class="person__role">Floral Designer/Creator</p>
    </div>
    <div class="contact">
      <div class="contact__icons" aria-hidden="true">
        <svg viewBox="0 0 24 24"><path d="M6.6 10.8a15.1 15.1 0 0 0 6.6 6.6l2.2-2.2a1 1 0 0 1 1-.25 11.4 11.4 0 0 0 3.6.57 1 1 0 0 1 1 1V20a1 1 0 0 1-1 1A17 17 0 0 1 3 4a1 1 0 0 1 1-1h3.5a1 1 0 0 1 1 1c0 1.25.2 2.45.57 3.57a1 1 0 0 1-.25 1z"/></svg>
        <svg viewBox="0 0 24 24"><path d="M2 5h20v14H2z M2 5l10 8 10-8" fill="none" stroke="#222" stroke-width="0"/><path d="M2 6.5V19h20V6.5l-10 7.5z"/><path d="M2.5 5h19L12 12.2z"/></svg>
        <svg viewBox="0 0 24 24"><circle cx="12" cy="12" r="10"/><path d="M2 12h20M12 2c3 3 3 17 0 20M12 2c-3 3-3 17 0 20" stroke="#f2f2f2" stroke-width="1.5" fill="none"/></svg>
      </div>
      <p class="contact__line">0418657203</p>
      <p class="contact__line">mara@tenderthorns.com</p>
      <p class="contact__line">www.tenderthorns.com</p>
    </div>
  </section>

  <section class="card card--back" aria-label="Business card back">
    <div class="back-mark" aria-hidden="true"></div>
    <p class="brand-name">TENDER THORNS</p>
  </section>
</main>
</body>
</html>
```